Private Optometric Practice Needs new Presentation Folders/Stationary

We recently moved our office and are looking to refresh our presentation folders and stationary. I tend to prefer simple, clean designs. We are a full scope optometric practice provide high quality eyewear, custom contact lenses, along with emergency care and treatment for dry eyes. We communicate with a lot of other doctors and want to exude professionalism. I have attached 2 versions of our logo.

Target Market(s)

Familys

Industry/Entity Type

Eyecare

Font styles to use
Sans Serif

Colors
0054AA
0677BA
7BADD7
CADEEF
E8F1F8

Requirements
Nice to have
• Bifold, areas to put information about practice, welcome letter

```html
<!DOCTYPE html>
<html lang="en">
<head>
<meta charset="utf-8">
<title>Brightline Eyecare Stationery</title>
<link rel="stylesheet" href="https://fonts.googleapis.com/css2?family=Poppins:wght@400;500;600;700&display=swap">
<style>
  :root {
    --sky: #36a9e0;
    --deep: #0677ba;
    --navy: #0054aa;
    --ink: #1f1f1f;
    --grey: #6d6e71;
    --paper: #ffffff;
    --bg-top: #f8f8f9;
    --bg-bottom: #e8e8ea;
  }
  * { margin: 0; padding: 0; box-sizing: border-box; }
  html, body { width: 1200px; height: 721px; overflow: hidden; }
  body {
    position: relative;
    font-family: "Poppins", sans-serif;
    color: var(--ink);
    background: linear-gradient(180deg, var(--bg-top), var(--bg-bottom));
  }
  .sheet {
    position: absolute;
    background: var(--paper);
    box-shadow: 0 1px 4px rgba(0,0,0,0.08);
    overflow: hidden;
  }
  .brand {
    position: absolute;
    display: flex;
    align-items: center;
    gap: 4px;
    font-weight: 500;
    color: var(--sky);
    white-space: nowrap;
    letter-spacing: 0.12em;
  }
  .brand .dot {
    display: inline-block;
    border-radius: 50%;
    background: var(--sky);
  }

  /* Envelope */
  .envelope { left: 78px; top: 141px; width: 357px; height: 155px; }
  .envelope .brand { left: 19px; top: 16px; font-size: 7px; }
  .envelope .brand .dot { width: 7px; height: 7px; }
  .envelope .window {
    position: absolute; left: 21px; top: 80px; width: 99px; height: 56px;
    border-radius: 4px;
    border: 1px solid #d2d2d4;
    background: linear-gradient(120deg, #dcdcde 0%, #efeff0 40%, #d8d8da 60%, #e6e6e8 100%);
    font-size: 5px; color: #777;
    padding: 18px 0 0 11px;
    line-height: 1.75;
  }
  .envelope .window b { color: #555; font-weight: 600; }
  .envelope .window .addr { padding-left: 10px; }

  /* Business cards */
  .card { top: 327px; width: 132px; height: 75px; }
  .card-front { left: 139px; }
  .card-front .brand { left: 0; right: 0; top: 31px; justify-content: center; font-size: 9px; }
  .card-front .brand .dot { width: 8px; height: 8px; }
  .card-back { left: 303px; }
  .card-back .mark {
    position: absolute; left: 18px; top: 32px; width: 12px; height: 12px;
    border-radius: 50%; background: var(--sky);
  }
  .card-back .contact { position: absolute; left: 54px; top: 23px; font-size: 3.4px; color: var(--grey); line-height: 1.35; }
  .card-back .contact .name { font-size: 4px; font-weight: 600; color: #444; margin-bottom: 3px; }
  .card-back .contact .row { display: flex; gap: 2px; align-items: flex-start; }
  .card-back .contact .row svg { width: 3px; height: 3px; margin-top: 0.4px; flex: none; }
  .card-back .wave { position: absolute; left: 0; bottom: 0; width: 132px; height: 12px; }

  /* Letterhead */
  .letterhead { left: 468px; top: 141px; width: 311px; height: 439px; }
  .letterhead .brand { left: 34px; top: 38px; font-size: 9px; }
  .letterhead .brand .dot { width: 8px; height: 8px; }
  .letter { position: absolute; left: 33px; top: 90px; width: 246px; font-size: 5.2px; line-height: 8.9px; color: #333; }
  .letter .recipient { font-size: 5.4px; }
  .letter .recipient b { font-weight: 500; color: var(--ink); }
  .letter .recipient .addr { padding-left: 10px; }
  .letter .date { position: absolute; right: 0; top: 1px; font-weight: 500; font-size: 5.4px; color: var(--ink); }
  .letter .subject { margin-top: 34px; }
  .letter .topic { margin-top: 17px; }
  .letter p { margin-top: 9px; text-align: justify; }
  .letter .signoff { margin-top: 17px; }
  .letter .practice { margin-top: 18px; font-weight: 500; color: var(--ink); }
  .letterhead .wave { position: absolute; left: 0; bottom: 0; width: 311px; height: 26px; }

  /* Folder */
  .folder { left: 812px; top: 141px; width: 311px; height: 439px; }
  .folder .brand { left: 0; right: 0; top: 104px; justify-content: center; font-size: 12px; }
  .folder .brand .dot { width: 11px; height: 11px; }
  .folder .wave { position: absolute; left: 0; top: 160px; width: 311px; height: 279px; }
  .folder .cover-title {
    position: absolute; left: 0; right: 0; top: 280px; text-align: center; color: #fff;
  }
  .folder .cover-title h1 { font-size: 16px; font-weight: 700; line-height: 16px; }
  .folder .cover-title .desc { font-size: 7.5px; margin-top: 4px; }
</style>
</head>
<body>

  <section class="sheet envelope">
    <div class="brand"><span class="dot"></span>BRIGHTLINE EYECARE</div>
    <div class="window">
      <div><b>To : Ms.</b> Partner</div>
      <div class="addr">123 Sample Address Here</div>
    </div>
  </section>

  <section class="sheet card card-front">
    <div class="brand"><span class="dot"></span>BRIGHTLINE EYECARE</div>
  </section>

  <section class="sheet card card-back">
    <span class="mark"></span>
    <div class="contact">
      <div class="name">DANIEL WHITFORD, O.D.</div>
      <div class="row">
        <svg viewBox="0 0 10 10"><path d="M5 0.5 L9.5 4.5 H8 V9.5 H2 V4.5 H0.5 Z" fill="#36a9e0"/></svg>
        <div>4120 LAKESIDE AVE.<br>SUITE B<br>FAIRHAVEN, MI 48300</div>
      </div>
      <div class="row">
        <svg viewBox="0 0 10 10"><path d="M2 0.5 L4 2.5 L3 4 Q4.5 6 6 7 L7.5 6 L9.5 8 L8 9.5 Q3 9 0.5 2 Z" fill="#36a9e0"/></svg>
        <div>555-014-2290</div>
      </div>
      <div class="row">
        <svg viewBox="0 0 10 10"><circle cx="5" cy="5" r="4.5" fill="#36a9e0"/></svg>
        <div>WWW.BRIGHTLINEEYECARE.COM</div>
      </div>
    </div>
    <svg class="wave" viewBox="0 0 132 12" preserveAspectRatio="none">
      <defs>
        <linearGradient id="cardBand" x1="0" x2="1" y1="0" y2="0">
          <stop offset="0" stop-color="#36a9e0"/>
          <stop offset="1" stop-color="#0677ba"/>
        </linearGradient>
      </defs>
      <path d="M0 8 Q40 12 80 5 Q110 1 132 6 V12 H0 Z" fill="url(#cardBand)"/>
      <path d="M0 6 Q40 10 80 3.5 Q110 -0.5 132 4.5" fill="none" stroke="#9a9a9a" stroke-width="0.3"/>
    </svg>
  </section>

  <section class="sheet letterhead">
    <div class="brand"><span class="dot"></span>BRIGHTLINE EYECARE</div>
    <div class="letter">
      <div class="recipient">
        <div><b>To : Ms. Partner</b></div>
        <div class="addr">123 Sample Address Here, City</div>
      </div>
      <div class="date">Date : January 04, 2021</div>
      <div class="subject">Sample Document Subject<br>Department Sample</div>
      <div class="topic">Here is the subject of the letter</div>
      <p style="margin-top:9px">Dear Ms. Partner,</p>
      <p>This is dummy text. It is only used to illustrate the gray value of the type. But is that really the case? Isn't it the same if I write "this is dummy text" or "Guaredisch nedunfeg"? FegCuned – not at all.</p>
      <p>Dummy text provides important information, like the legibility of the body text, the impression it makes on the reader, the harmony between the individual figures, how narrow or wide they appear. Dummy text should contain as many different letters as possible and should be written in the original language. It doesn't have to make sense, it just needs to be readable. Texts in foreign languages, like "Lorem ipsum", don't actually serve this purpose, as they provide a false impression of what the body text actually looks like. This is dummy text. It is only used to illustrate the gray value of the type. But is that really the case? Isn't it the same if I write "this is dummy text" or "Guaredisch nedunfeg"? Fegeuned – not at all.</p>
      <div class="signoff">Yours sincerely,<br>SAMPLE AG</div>
      <div class="practice">Brightline Eyecare</div>
    </div>
    <svg class="wave" viewBox="0 0 311 26" preserveAspectRatio="none">
      <path d="M0 12 Q60 20 150 11 Q230 1 311 10 V26 H0 Z" fill="#36a9e0"/>
      <path d="M0 9 Q60 17 150 8 Q230 -2 311 7" fill="none" stroke="#8a8a8a" stroke-width="0.5"/>
    </svg>
  </section>

  <section class="sheet folder">
    <div class="brand"><span class="dot"></span>BRIGHTLINE EYECARE</div>
    <svg class="wave" viewBox="0 0 311 279" preserveAspectRatio="none">
      <path d="M0 18 Q70 26 160 14 Q250 2 311 15 V279 H0 Z" fill="#36a9e0"/>
      <path d="M0 15 Q70 23 160 11 Q250 -1 311 12" fill="none" stroke="#8a8a8a" stroke-width="0.5"/>
    </svg>
    <div class="cover-title">
      <h1>YOUR DOCUMENT<br>TITLE HERE</h1>
      <div class="desc">Description here</div>
    </div>
  </section>

</body>
</html>
```